Mt Halloway Hotel

We need a business card with old world charm.
The design will need to promote dining and accommodation for local residents as a place to relax and for vacationing or week-end visitors seeking an experience of country hospitality.
The hotel was originally opened in 1909.

Target Market(s)

Adults and Families searching for dining and accommodation.

Industry/Entity Type

Business

Requirements
Nice to have
• Sketch or line drawing of Hotel

```html
<!DOCTYPE html>
<html lang="en">
<head>
<meta charset="utf-8">
<title>Mt Halloway Hotel – Business Card</title>
<link rel="stylesheet" href="https://fonts.googleapis.com/css2?family=Berkshire+Swash&family=Open+Sans:wght@400&display=swap">
<style>
  :root {
    --card-bg: #869aa0;
    --ink-purple: #4a0c9e;
    --frame-silver: #e4e8ea;
    --frame-shadow: #5d6a70;
    --photo-dark: #2a2228;
    --photo-brick: #5a2a30;
    --photo-sky: #8a9aa8;
    --ornament-cream: #dfe3d6;
  }
  * { margin: 0; padding: 0; box-sizing: border-box; }
  html, body {
    width: 1200px;
    height: 783px;
    overflow: hidden;
    background: var(--card-bg);
  }
  .business-card {
    position: relative;
    width: 1200px;
    height: 783px;
    background: var(--card-bg);
    color: var(--ink-purple);
    font-family: "Open Sans", Verdana, sans-serif;
  }
  .hotel-portrait {
    position: absolute;
    left: 404px;
    top: 118px;
    width: 396px;
    height: 240px;
  }
  .ornament {
    position: absolute;
    top: 378px;
    width: 228px;
    height: 88px;
  }
  .ornament--left { left: 83px; }
  .ornament--right { left: 880px; }
  .hotel-name {
    position: absolute;
    left: 0;
    width: 100%;
    top: 384px;
    text-align: center;
    font-family: "Berkshire Swash", cursive;
    font-weight: 400;
    font-size: 54px;
    line-height: 1;
    color: var(--ink-purple);
  }
  .established {
    position: absolute;
    left: 0;
    width: 100%;
    top: 470px;
    text-align: center;
    font-size: 25px;
    letter-spacing: 0.5px;
  }
  .contact {
    position: absolute;
    top: 592px;
    font-size: 25px;
    line-height: 38px;
    letter-spacing: 0.6px;
    list-style: none;
  }
  .contact--address { left: 88px; }
  .contact--online { right: 85px; top: 630px; text-align: right; }
</style>
</head>
<body>
<main class="business-card">
  <svg class="hotel-portrait" viewBox="0 0 396 240" role="img" aria-label="Photograph of the historic brick hotel building in an oval frame">
    <defs>
      <linearGradient id="photoTone" x1="0" y1="0" x2="0" y2="1">
        <stop offset="0" stop-color="var(--photo-sky)"/>
        <stop offset="0.35" stop-color="var(--photo-brick)"/>
        <stop offset="1" stop-color="var(--photo-dark)"/>
      </linearGradient>
    </defs>
    <ellipse cx="198" cy="122" rx="192" ry="110" fill="var(--frame-shadow)"/>
    <ellipse cx="198" cy="120" rx="190" ry="108" fill="none" stroke="var(--frame-silver)" stroke-width="12"/>
    <ellipse cx="198" cy="120" rx="178" ry="96" fill="url(#photoTone)"/>
  </svg>

  <svg class="ornament ornament--left" viewBox="0 0 228 88" role="img" aria-label="Decorative swirl ornament">
    <path d="M0 50 C60 30 110 0 170 10 C205 16 228 36 228 46 C228 58 205 76 170 82 C110 92 60 62 0 50 Z" fill="var(--ornament-cream)"/>
  </svg>

  <h1 class="hotel-name">Mt Halloway Hotel</h1>

  <svg class="ornament ornament--right" viewBox="0 0 228 88" role="img" aria-label="Decorative swirl ornament">
    <path d="M0 50 C60 30 110 0 170 10 C205 16 228 36 228 46 C228 58 205 76 170 82 C110 92 60 62 0 50 Z" fill="var(--ornament-cream)"/>
  </svg>

  <p class="established">Established 1909</p>

  <ul class="contact contact--address">
    <li>1234 Any Road</li>
    <li>Mt Halloway NSW 2000</li>
    <li>Telephone:+61 2345 6789</li>
  </ul>

  <ul class="contact contact--online">
    <li>info@mthallowayhotel.com</li>
    <li>www.mthallowayhotel.com</li>
  </ul>
</main>
</body>
</html>
```